Flyer-Design für Food Truck Party Veranstaltung gesucht
Zielgruppe
Wir haben einen Food Truck und werden zum zweiten Mal in diesem Jahr für 7 Wochen ein Pop-Up Restaurant eröffnen!(Flyer für das erste Pop-Up Restaurant ist als Beispiel beigefügt, nur um zu verdeutlichen was wir machen, soll nicht so übernommen werden! Denn hier wird eher eine Party, als ein Restaurant suggeriert)
Zielgruppe sind Personen, die zwischen 30-70 Jahren sind, gerne Geld für gutes, modernes Essen ausgeben, und die offen sind für ein Restaurant, das nur temporär geöffnet ist.
Aufgabenstellung
Unser Logo findet ihr im Dateiupload. Unser Restaurant ist eine alte, aber sehr coole Lagerhalle, die wie ein modernes, gemütliches, lockeres, gehobenes Restaurant eingerichtet ist. Dies sollte auch der Flyer suggerieren! Der Food Truck steht vor dem Restaurant und dient als Küche. Bevorzugt ist das Format DIN-Lang (10,9 x 21,4 Dateiformat, 10,5 x 21,0 Endformat)
Datum: 13.05.17 - 02.07.17
immer von Donnerstags bis Sonntags
Donnerstags: Deluxe Burger & Wine
Freitags bis Sonntags: jedes Wochenende eine neue, kompakte Speisekarte mit modernen Tellergerichten
Uhrzeit: 18.00 - 23.00 Uhr
Küchenzeit: 18.00 - 21.00 Uhr
Internetadresse: www.pelmar.ruhr
facebook: pelmarkuechenwagen

```html
<!DOCTYPE html>
<html lang="de">
<head>
<meta charset="utf-8">
<title>pelmar – Pop-Up Restaurant Flyer</title>
<link href="https://fonts.googleapis.com/css2?family=Tinos:wght@400;700&family=Alex+Brush&family=Shadows+Into+Light&display=swap" rel="stylesheet">
<style>
  :root{
    --stage:#a4a4a4;
    --black:#0c0c0c;
    --panel:#141414;
    --gold:#c9a24a;
    --gold-bright:#f2c21b;
    --gold-deep:#a8853a;
    --white:#f5f5f5;
    --photo-light:#9a9a9a;
    --photo-dark:#2a2a2a;
  }
  *{box-sizing:border-box;margin:0;padding:0}
  html,body{width:1184px;height:1200px;overflow:hidden}
  body{background:var(--stage);position:relative;font-family:"Tinos",serif;color:var(--white)}
  .flyer{position:absolute;top:45px;width:500px;height:1110px;background:var(--black);overflow:hidden}
  .flyer--front{left:62px;width:520px}
  .flyer--back{left:622px}
  .photo{position:absolute;left:0;width:100%}
  .shapes{position:absolute;inset:0}

  /* front */
  .topbar{position:absolute;left:0;right:0;top:33px;height:43px;background:var(--panel);
    border-top:2px solid var(--gold);border-bottom:2px solid var(--gold);
    display:flex;justify-content:space-between;align-items:center;padding:0 12px 0 18px;font-size:18px}
  .topbar__item{display:flex;align-items:center;gap:7px}
  .icon-square{width:9px;height:14px;background:var(--white)}
  .icon-circle{width:22px;height:22px;border:1.5px solid var(--white);border-radius:50%}
  .logo{position:absolute;text-align:center;color:var(--gold-bright)}
  .logo__name{font-size:40px;line-height:1;display:block}
  .logo__tag{font-size:6px;letter-spacing:2px;color:var(--white);display:block;margin-top:6px}
  .logo--front{left:0;width:180px;top:738px}
  .dates{position:absolute;left:220px;width:280px;top:625px;text-align:center;color:var(--gold);font-weight:700}
  .dates__day{font-size:76px;line-height:78px;display:block}
  .dates__sep{font-family:"Shadows Into Light",cursive;font-weight:400;color:var(--gold-bright);font-size:30px;line-height:30px;display:block;margin:-6px 0 -4px}
  .year{position:absolute;font-weight:700;font-size:36px;transform:rotate(-90deg);color:var(--white)}
  .year--front{left:463px;top:702px}
  .headline{position:absolute;left:0;right:0;top:895px;text-align:center;font-weight:700;line-height:1}
  .headline__top{font-size:66px;display:block}
  .headline__bottom{font-size:55px;display:block;margin-top:8px}
  .tagline{position:absolute;right:14px;top:1040px;font-family:"Shadows Into Light",cursive;font-size:30px;transform:rotate(-9deg);transform-origin:right}

  /* back */
  .logo--back{left:97px;width:218px;top:48px}
  .intro{position:absolute;left:56px;right:20px;font-size:16px;line-height:18px}
  .script{font-family:"Alex Brush",cursive;color:var(--gold-bright);font-size:36px;line-height:1}
  .intro--restaurant{top:215px}
  .intro--truck{top:318px}
  .offer{position:absolute;left:0;top:459px;width:500px;height:184px;background:var(--black);
    border-top:3px solid var(--gold);border-bottom:3px solid var(--gold)}
  .offer__body{position:absolute;left:60px;width:370px;top:28px;text-align:center;font-size:16px;line-height:19px}
  .offer__body .script{font-size:38px;display:block}
  .offer__weekend{margin-top:26px}
  .year--back{left:448px;top:70px}
  .facts{position:absolute;left:56px;top:748px;font-size:16px;line-height:20px}
  .facts .script{font-size:34px;display:block;margin-bottom:4px}
  .facts__group{margin-bottom:12px}
</style>
</head>
<body>

<section class="flyer flyer--front">
  <div class="photo" style="top:0;height:700px;background:radial-gradient(ellipse at 60% 30%,#d8d8d8 0%,#8a8a8a 30%,#3a3a3a 70%,#1a1a1a 100%)" role="img" aria-label="Schwarzweißfoto: Glasvase mit Gerbera neben Flaschen auf einem Tisch"></div>
  <header class="topbar">
    <span class="topbar__item"><span class="icon-square"></span>pelmarkuechenwagen</span>
    <span class="topbar__item"><span class="icon-circle"></span>www.pelmar.ruhr</span>
  </header>
  <svg class="shapes" viewBox="0 0 520 1110" aria-hidden="true">
    <rect x="0" y="828" width="520" height="282" fill="var(--black)"/>
    <polygon points="197,618 520,618 520,830 178,830" fill="var(--panel)"/>
    <polyline points="520,618 197,618 178,690" fill="none" stroke="var(--gold)" stroke-width="3"/>
    <line x1="178" y1="830" x2="520" y2="830" stroke="var(--gold)" stroke-width="3"/>
    <polygon points="0,672 215,672 166,867 0,867" fill="var(--black)"/>
    <polyline points="0,672 215,672 166,867 0,867" fill="none" stroke="var(--gold)" stroke-width="3"/>
  </svg>
  <div class="logo logo--front">
    <span class="logo__name">pelmar</span>
    <span class="logo__tag">POP-UP RESTAURANT</span>
  </div>
  <div class="dates">
    <span class="dates__day">13.05.</span>
    <span class="dates__sep">bis zum</span>
    <span class="dates__day">02.07.</span>
  </div>
  <span class="year year--front">2017</span>
  <h1 class="headline"><span class="headline__top">POP-UP</span><span class="headline__bottom">RESTAURANT</span></h1>
  <p class="tagline">powered by food truck</p>
</section>

<section class="flyer flyer--back">
  <div class="photo" style="top:0;height:460px;background:linear-gradient(90deg,#2b2b2b 0%,#3c3c3c 55%,#8e8e8e 80%,#5a5a5a 100%)" role="img" aria-label="Schwarzweißfoto: Backsteinfassade der alten Lagerhalle mit Sprossenfenster"></div>
  <div class="photo" style="top:643px;height:467px;background:linear-gradient(180deg,#3a3a3a 0%,#222 40%,#151515 100%)" role="img" aria-label="Schwarzweißfoto: Innenraum der Lagerhalle mit Holzbalken"></div>
  <svg class="shapes" viewBox="0 0 500 1110" aria-hidden="true">
    <polygon points="97,0 315,0 315,204 206,126 97,204" fill="var(--black)" stroke="var(--gold)" stroke-width="3"/>
  </svg>
  <div class="logo logo--back">
    <span class="logo__name">pelmar</span>
    <span class="logo__tag">POP-UP RESTAURANT</span>
  </div>
  <p class="intro intro--restaurant"><span class="script">Restaurant</span> die wie ein modernes, gemütliches, lockeres, gehobenes Restaurant eingerichtet ist.</p>
  <p class="intro intro--truck"><span class="script">Food Truck</span> steht vor dem Restaurant und dient als Küche.</p>
  <div class="offer">
    <div class="offer__body">
      <span class="script">Donnerstags</span>
      Deluxe Burger &amp; Wine
      <p class="offer__weekend">Freitags bis Sonntags: jedes WE eine neue, kompakte Speisekarte mit modernen Tellergerichten</p>
    </div>
    <span class="year year--back">2017</span>
  </div>
  <div class="facts">
    <div class="facts__group"><span class="script">Location</span>Kesselweg 12<br>Essen-Kettwig</div>
    <div class="facts__group"><span class="script">Wann</span>Donnerstags bis Sonntags<br>18.00 - 23.00 Uhr</div>
    <div class="facts__group"><span class="script">Küchenzeiten</span>Donnerstags bis Sonntags<br>18.00 - 21.00 Uhr</div>
    <div class="facts__group"><span class="script">Reservierung</span>Sichere Deine Plätze unter:<br>0170 - 55 41 203</div>
  </div>
</section>

</body>
</html>
```